IT Company need facebook graphics

We need a facebook logo and cover that matches more our website and other marketing materials which is quite uniform in colours.
We are a small company, we do not advertise much mainly word of mouth, but we want to try out some Facebook advertising and need our page to look amazing.
Something playful yet professional, something that will stand out in peoples mind.
Target Market(s)
Home users and small business
Industry/Entity Type
Computer Repair
Requirements
Must have
- A colour scheme to match existing website, but be playful and fun. Website is www.mzpalisade.com.au
Nice to have
- No input for nice to have, I trust the awesome talent out there to come up with something.
Should not have
- Again, no input for should not haves.

```html
<!DOCTYPE html>
<html lang="en">
<head>
<meta charset="utf-8">
<title>Palisade Computer – Facebook Cover</title>
<link href="https://fonts.googleapis.com/css2?family=Open+Sans:wght@400;600&family=PT+Sans+Narrow:wght@700&display=swap" rel="stylesheet">
<style>
  :root {
    --brand-yellow: #fcc200;
    --brand-yellow-deep: #e3a900;
    --ink: #1c1c1c;
    --panel-grey: #d6d6d6;
    --panel-grey-light: #ececec;
    --footer-cream: #fbf8ee;
    --photo-server: #4d6f9a;
    --photo-server-dark: #1e2c44;
    --photo-code: #0f2a4a;
    --photo-code-light: #3f78b0;
    --white: #ffffff;
  }
  html, body {
    margin: 0;
    padding: 0;
    overflow: hidden;
    background: var(--white);
  }
  .cover {
    position: relative;
    width: 1200px;
    height: 444px;
    overflow: hidden;
    font-family: "Open Sans", Arial, sans-serif;
    color: var(--ink);
  }
  .cover__art {
    position: absolute;
    inset: 0;
  }
  .cover__ribbon {
    position: absolute;
    left: 448px;
    top: 0;
    width: 314px;
    height: 256px;
  }
  .brand {
    position: absolute;
    left: 448px;
    top: 98px;
    width: 314px;
    text-align: center;
    font-size: 28px;
    font-weight: 400;
    color: var(--ink);
    margin: 0;
  }
  .tagline {
    position: absolute;
    left: 300px;
    top: 278px;
    width: 600px;
    margin: 0;
    text-align: center;
    font-family: "PT Sans Narrow", "Arial Narrow", sans-serif;
    font-weight: 700;
    font-size: 31px;
    line-height: 40px;
    text-transform: uppercase;
    color: var(--ink);
  }
  .footer {
    position: absolute;
    left: 0;
    top: 374px;
    width: 1200px;
    height: 70px;
    background: var(--footer-cream);
  }
  .contact-phone {
    position: absolute;
    left: 490px;
    top: 22px;
    display: flex;
    align-items: center;
    gap: 8px;
    font-size: 22px;
    font-weight: 600;
    color: var(--ink);
  }
  .social {
    position: absolute;
    top: 19px;
    width: 30px;
    height: 30px;
    border-radius: 5px;
    background: var(--brand-yellow);
  }
  .social--first { left: 1017px; }
  .social--second { left: 1109px; }
</style>
</head>
<body>
<div class="cover">
  <svg class="cover__art" width="1200" height="444" viewBox="0 0 1200 444" aria-hidden="false">
    <defs>
      <linearGradient id="panelGrey" x1="0" y1="0" x2="0" y2="1">
        <stop offset="0" stop-color="var(--panel-grey-light)"/>
        <stop offset="1" stop-color="var(--panel-grey)"/>
      </linearGradient>
      <linearGradient id="serverRoom" x1="0" y1="0" x2="1" y2="1">
        <stop offset="0" stop-color="var(--photo-server-dark)"/>
        <stop offset="0.55" stop-color="var(--photo-server)"/>
        <stop offset="1" stop-color="#b9c6d6"/>
      </linearGradient>
      <linearGradient id="codeScene" x1="0" y1="0" x2="1" y2="1">
        <stop offset="0" stop-color="var(--photo-code)"/>
        <stop offset="0.5" stop-color="var(--photo-code-light)"/>
        <stop offset="1" stop-color="#3b2a1f"/>
      </linearGradient>
    </defs>

    <rect class="panel" x="0" y="0" width="1200" height="374" fill="url(#panelGrey)"/>

    <path class="swoosh swoosh--left" d="M0 312 Q270 300 500 60 L500 90 Q280 318 0 330 Z" fill="var(--brand-yellow)"/>
    <path class="swoosh swoosh--right" d="M1200 312 Q930 300 700 60 L700 90 Q920 318 1200 330 Z" fill="var(--brand-yellow)"/>

    <path class="photo photo--left" role="img" aria-label="Photo of two technicians inspecting server racks in a data centre"
          d="M0 0 H500 V60 Q270 300 0 312 Z" fill="url(#serverRoom)"/>
    <path class="photo photo--right" role="img" aria-label="Photo of a young man working at a computer with streams of binary digits"
          d="M1200 0 H700 V60 Q930 300 1200 312 Z" fill="url(#codeScene)"/>
  </svg>

  <svg class="cover__ribbon" width="314" height="256" viewBox="0 0 314 256">
    <path d="M0 0 H314 V256 L157 212 L0 256 Z" fill="var(--brand-yellow)"/>
    <path d="M10 236 L157 196 L304 236" fill="none" stroke="var(--white)" stroke-width="2" stroke-dasharray="7 5"/>
    <circle cx="157" cy="62" r="24" fill="none" stroke="var(--ink)" stroke-width="3"/>
  </svg>

  <p class="brand">Palisade Computer</p>

  <h1 class="tagline">One stop shop for all<br>your IT needs</h1>

  <footer class="footer">
    <div class="contact-phone">
      <svg width="24" height="24" viewBox="0 0 24 24" aria-hidden="true">
        <path d="M6.6 3.5 L9.3 6.6 C9.8 7.2 9.7 8 9.1 8.5 L7.9 9.5 C8.9 11.8 11.2 14.1 13.6 15.2 L14.6 14 C15.1 13.4 15.9 13.3 16.5 13.8 L19.6 16.5 C20.2 17 20.2 17.9 19.7 18.5 L18.3 20 C17.6 20.7 16.6 21 15.6 20.7 C9.8 19 4.9 14.1 3.3 8.4 C3 7.4 3.3 6.4 4 5.7 L5.5 4.2 C5.8 3.6 6.1 3.4 6.6 3.5 Z"
              fill="none" stroke="var(--ink)" stroke-width="1.6" stroke-linejoin="round"/>
      </svg>
      <span>+1300 555 018</span>
    </div>
    <span class="social social--first" aria-label="Social page"></span>
    <span class="social social--second" aria-label="Social page"></span>
  </footer>
</div>
</body>
</html>
```